Construction business card

We are a family run and family oriented business in Philadelphia and we are starting new. We proudly serve the public by giving our customers great work at affordable prices. We can do all aspects of construction from the roof to the basement. We would like our business card to incorporate tools and family.
Updates

Can y'all please incorporate a bulldog

Industry/Entity Type

Construction

Contact Information for Business Card

Harbor Builders LLC, Dennis Whitcomb, 1187 W 9th st Philadelphia Pa 19140, CEO Main phone (215) 555-0143 cellphone 215-555-0187 Dennis whitcomb Jr cellphone 267-555-0129 email harborbuildersllc@quillpost.example

Colors
f78f20
ffffff
1b1b1b

```html
<!DOCTYPE html>
<html lang="en">
<head>
<meta charset="utf-8">
<title>Harbor Builders LLC — Business Card</title>
<link rel="stylesheet" href="https://fonts.googleapis.com/css2?family=Questrial&display=swap">
<style>
  :root {
    --orange: #f78f20;
    --white: #ffffff;
    --ink: #1b1b1b;
    --stage: #ececec;
    --faint: #c9c9c9;
    --silhouette-light: #e2e2e2;
    --silhouette-dark: #c4c4c4;
  }
  * { box-sizing: border-box; margin: 0; padding: 0; }
  html, body { width: 1200px; height: 784px; overflow: hidden; background: var(--stage); }
  body { font-family: "Questrial", "Century Gothic", sans-serif; color: var(--ink); }

  .card {
    position: absolute; top: 229px;
    width: 570px; height: 326px;
    background: var(--white);
    box-shadow: 0 4px 16px rgba(0,0,0,.12);
    overflow: hidden;
  }
  .card-back { left: 20px; }
  .card-front { left: 610px; }

  /* Back side */
  .back-brand {
    position: absolute; inset: 0;
    display: flex; align-items: center; justify-content: center; gap: 14px;
  }
  .back-brand .brand-mark { width: 30px; height: 30px; background: var(--faint); }
  .back-brand .brand-name { font-size: 44px; color: var(--faint); letter-spacing: 1px; }

  /* Front side */
  .holder { position: absolute; right: 22px; top: 14px; text-align: right; }
  .holder-name { color: var(--orange); font-size: 16px; font-weight: 700; }
  .holder-title { font-size: 11px; margin-top: 2px; }

  .front-brand {
    position: absolute; left: 48px; top: 84px;
    display: flex; align-items: center; gap: 10px;
  }
  .front-brand .brand-mark { width: 20px; height: 20px; background: var(--orange); }
  .front-brand .brand-name { font-size: 28px; color: var(--ink); letter-spacing: .5px; }

  .family-art {
    position: absolute; left: 400px; top: 72px;
    width: 160px; height: 195px;
    background: linear-gradient(180deg, var(--silhouette-light), var(--silhouette-dark));
    border-radius: 60px 60px 0 0;
  }

  .contacts { position: absolute; left: 40px; top: 160px; list-style: none; }
  .contacts li {
    display: flex; align-items: center; gap: 7px;
    font-size: 15px; line-height: 20px; height: 20px; white-space: nowrap;
  }
  .contacts svg { width: 13px; height: 13px; fill: var(--orange); flex: none; }
  .contacts .accent { color: var(--orange); }

  .band-rule { position: absolute; left: 0; width: 100%; height: 3px; background: var(--orange); }
  .band-rule.top { top: 267px; }
  .band-rule.bottom { top: 296px; }
  .band { position: absolute; left: 0; top: 270px; width: 100%; height: 26px; background: var(--ink); }
</style>
</head>
<body>
  <section class="card card-back" aria-label="Card back">
    <div class="back-brand">
      <span class="brand-mark"></span>
      <span class="brand-name">Harbor Builders LLC</span>
    </div>
  </section>

  <section class="card card-front" aria-label="Card front">
    <div class="holder">
      <div class="holder-name">Dennis Whitcomb</div>
      <div class="holder-title">CEO</div>
    </div>

    <div class="front-brand">
      <span class="brand-mark"></span>
      <span class="brand-name">Harbor Builders LLC</span>
    </div>

    <div class="family-art" role="img" aria-label="Grey silhouette of a family holding hands with a bulldog"></div>

    <ul class="contacts">
      <li>
        <svg viewBox="0 0 24 24" aria-hidden="true"><path d="M6.6 10.8a15.1 15.1 0 0 0 6.6 6.6l2.2-2.2c.3-.3.7-.4 1-.2 1.1.4 2.3.6 3.6.6.6 0 1 .4 1 1V20c0 .6-.4 1-1 1A17 17 0 0 1 3 4c0-.6.4-1 1-1h3.5c.6 0 1 .4 1 1 0 1.3.2 2.5.6 3.6.1.3 0 .7-.2 1z"/></svg>
        <span>(215) 555-0143</span>
      </li>
      <li>
        <svg viewBox="0 0 24 24" aria-hidden="true"><path d="M7 1h10a2 2 0 0 1 2 2v18a2 2 0 0 1-2 2H7a2 2 0 0 1-2-2V3a2 2 0 0 1 2-2zm0 4v13h10V5zm5 14.5a1 1 0 1 0 0 2 1 1 0 0 0 0-2z"/></svg>
        <span>215-555-0187</span>
      </li>
      <li>
        <svg viewBox="0 0 24 24" aria-hidden="true"><path d="M7 1h10a2 2 0 0 1 2 2v18a2 2 0 0 1-2 2H7a2 2 0 0 1-2-2V3a2 2 0 0 1 2-2zm0 4v13h10V5zm5 14.5a1 1 0 1 0 0 2 1 1 0 0 0 0-2z"/></svg>
        <span><span class="accent">Dennis whitcomb Jr</span> 267-555-0129</span>
      </li>
      <li>
        <svg viewBox="0 0 24 24" aria-hidden="true"><path d="M2 5h20v14H2zm2 2v.5l8 5.5 8-5.5V7zm0 3v7h16v-7l-8 5.5z"/></svg>
        <span>harborbuildersllc@quillpost.example</span>
      </li>
      <li>
        <svg viewBox="0 0 24 24" aria-hidden="true"><path d="M12 2 1 12h3v10h6v-6h4v6h6V12h3z"/></svg>
        <span>1187 W 9th st Philadelphia Pa 19140</span>
      </li>
    </ul>

    <div class="band-rule top"></div>
    <div class="band"></div>
    <div class="band-rule bottom"></div>
  </section>
</body>
</html>
```